Unique, Impressive, and Modern Business Card

Looking for a distinctive, unique business card. We are distributors of tire repairs supplies, tools, machinery, and chemicals. Our target market are tire repair shops, tire franchises, and mechanic shops. We would like our design to include tire characteristics, and use our business colors. Feel free to use all types design and printing options (emboss, spot uv, foil, etc) QR code may be applied, you can use different size business cards ( standard, square, rounded edge, colored edge, etc), all formats needed for printing, also editable for future changes

Target Market(s)

Automotive, Tire industries

Industry/Entity Type

Tire Industry (automotive)

Contact Information for Business Card

Business logo, business Name (Corvane Supply Inc), Name (Marcus Pellow), Position (President) Address (58 Fernhollow Lane, Brentwood NY 11742), Contact number (Company 1-855-302-4418, Cell 1-631-245-9073, email address (marcus.pellow@corvanesupply.com), URL (www.corvanesupply.com

Requirements
Must have
• Must include Business Colors (Black, Green, Blue, White) see sample website file
Nice to have
• emboss, spot uv, etc

```html
<!DOCTYPE html>
<html lang="en">
<head>
<meta charset="utf-8">
<title>Corvane Supply Inc — Business Card</title>
<link href="https://fonts.googleapis.com/css2?family=Oswald:wght@700&family=Roboto:wght@400;500;700&display=swap" rel="stylesheet">
<style>
  :root {
    --bg: #e9e9e9;
    --card-white: #f6f6f6;
    --brand-blue: #2c40d9;
    --name-blue: #1f34d4;
    --ink: #151515;
    --paper-white: #ffffff;
  }
  * { box-sizing: border-box; margin: 0; padding: 0; }
  html, body {
    width: 1200px;
    height: 1000px;
    overflow: hidden;
    background: var(--bg);
  }
  .stage {
    position: relative;
    width: 1200px;
    height: 1000px;
    display: flex;
    align-items: center;
    justify-content: center;
    gap: 80px;
  }
  .card {
    position: relative;
    width: 420px;
    height: 420px;
    border-radius: 52px;
    overflow: hidden;
  }
  .card--front {
    background: var(--card-white);
    box-shadow: -2px 0 0 var(--brand-blue), 0 10px 30px rgba(0,0,0,0.12);
    font-family: "Roboto", sans-serif;
    color: var(--ink);
  }
  .card--back {
    background: var(--brand-blue);
    box-shadow: 0 10px 30px rgba(0,0,0,0.12);
    display: flex;
    align-items: center;
    justify-content: center;
  }
  .brand {
    display: flex;
    align-items: center;
    gap: 8px;
    font-family: "Roboto", sans-serif;
    font-weight: 500;
    letter-spacing: 0.06em;
    text-transform: uppercase;
    white-space: nowrap;
  }
  .brand__dot {
    border-radius: 50%;
    flex: none;
  }
  .card--front .brand {
    position: absolute;
    top: 54px;
    right: 34px;
    font-size: 15px;
    color: var(--ink);
  }
  .card--front .brand__dot {
    width: 22px;
    height: 22px;
    background: var(--brand-blue);
  }
  .card--back .brand {
    font-size: 26px;
    color: var(--paper-white);
    gap: 14px;
  }
  .card--back .brand__dot {
    width: 40px;
    height: 40px;
    background: var(--paper-white);
  }
  .identity {
    position: absolute;
    top: 150px;
    left: 52px;
  }
  .identity__name {
    font-family: "Oswald", sans-serif;
    font-weight: 700;
    font-size: 32px;
    line-height: 1;
    color: var(--name-blue);
    text-transform: uppercase;
    white-space: nowrap;
  }
  .identity__role {
    margin-top: 4px;
    font-weight: 700;
    font-size: 13px;
    letter-spacing: 0.04em;
    text-transform: uppercase;
  }
  .contact {
    position: absolute;
    top: 232px;
    left: 46px;
    right: 20px;
    font-size: 15px;
    line-height: 20px;
    font-weight: 400;
    font-style: normal;
    white-space: nowrap;
  }
  .contact__group + .contact__group { margin-top: 18px; }
</style>
</head>
<body>
<main class="stage">
  <section class="card card--front" aria-label="Business card front">
    <div class="brand">
      <span class="brand__dot"></span>
      <span class="brand__name">Corvane Supply</span>
    </div>
    <div class="identity">
      <h1 class="identity__name">Marcus Pellow</h1>
      <p class="identity__role">President</p>
    </div>
    <address class="contact">
      <div class="contact__group">
        <p>marcus.pellow@corvanesupply.com</p>
        <p>corvanesupply.com</p>
      </div>
      <div class="contact__group">
        <p>1-555-245-9073</p>
      </div>
      <div class="contact__group">
        <p>58 Fernhollow Lane, Larkfield PA 19382</p>
      </div>
    </address>
  </section>

  <section class="card card--back" aria-label="Business card back">
    <div class="brand">
      <span class="brand__dot"></span>
      <span class="brand__name">Corvane Supply</span>
    </div>
  </section>
</main>
</body>
</html>
```